Healthcare Technology Company Business Card Design

Hi,

We require a new business card design thats catchy and professional.
Our target audience is healthcare professionals. See supplied artwork for our logo.

If you think its achievable please try add the tag line, not necessary however.
"Building smarter clinical tools that lift patient care and practice efficiency"

We'll require the following information on the card. No need to have the subject titles but i've referenced them for your convenience.

Personal Details
Paul Dwyer
Position: Director
Phone Number - 03 9472 5836
Mobile Number - 0438 275 904
Email: firstname.lastname@mediqbay.com.au

Company Details
Suite 31, 286 Keldon Street
Kestrel Bay, Avonmere
Fax: 03 8241 3975
mediqbay.com.au

Prefer a thinner design than the normal stock standard business card dimensions.
Please ensure there is adequate bleed.

Target Market(s)

Healthcare Professionals

Industry/Entity Type

Healthcare

Font styles to use
Sans Serif

Requirements
Must have
• Clean, Sharp Looks
Should not have
• Any healthcare symbols

```html
<!DOCTYPE html>
<html lang="en">
<head>
<meta charset="utf-8">
<title>mediqbay business card</title>
<link href="https://fonts.googleapis.com/css2?family=Arimo:wght@400;700&display=swap" rel="stylesheet">
<style>
  :root {
    --bg: #e9eaec;
    --card: #f4f5f6;
    --navy: #1c3563;
    --navy-deep: #14305e;
    --navy-soft: #3d5a91;
    --orange: #ee8a1e;
    --ink: #23355c;
    --white: #ffffff;
    --social-1: #3aa3d8;
    --social-2: #4c6eaa;
    --social-3: #2e6fa8;
    --social-4: #1f5f93;
  }
  * { margin: 0; padding: 0; box-sizing: border-box; }
  html, body {
    width: 1200px; height: 900px; overflow: hidden;
    background: var(--bg);
    font-family: "Arimo", Arial, sans-serif;
  }
  .stage {
    width: 1200px; height: 900px;
    display: flex; flex-direction: column;
    align-items: center; justify-content: center; gap: 56px;
  }
  .card {
    width: 640px; height: 370px;
    position: relative;
    box-shadow: 0 6px 18px rgba(20, 30, 60, 0.14);
  }
  .card-front { background: var(--card); }
  .card-back { background: var(--navy-deep); overflow: hidden; }

  .brand {
    position: absolute; top: 44px; right: 52px;
    display: flex; align-items: center; gap: 12px;
  }
  .brand-mark { width: 30px; height: 30px; background: var(--orange); }
  .brand-name {
    font-weight: 700; font-size: 46px; letter-spacing: -1px;
    color: var(--navy);
  }

  .person { position: absolute; left: 58px; top: 150px; }
  .person-name {
    font-weight: 700; font-size: 21px; letter-spacing: 0.5px;
    color: var(--navy); text-transform: uppercase;
  }
  .person-role { font-size: 14px; color: var(--ink); margin-top: 3px; }

  .contact-list { list-style: none; margin-top: 14px; }
  .contact-item {
    display: flex; align-items: center; gap: 10px;
    font-size: 14px; color: var(--ink); line-height: 22px;
  }
  .contact-icon { width: 14px; height: 14px; flex: none; }
  .address { margin-top: 14px; font-size: 14px; color: var(--ink); }

  .social { position: absolute; right: 52px; top: 150px; display: flex; gap: 4px; }
  .social-badge { width: 18px; height: 18px; }
  .social-badge:nth-child(1) { background: var(--social-1); }
  .social-badge:nth-child(2) { background: var(--social-2); }
  .social-badge:nth-child(3) { background: var(--social-3); }
  .social-badge:nth-child(4) { background: var(--social-4); }

  .back-name {
    position: absolute; top: 96px; left: 0; right: 0;
    text-align: center;
    font-weight: 700; font-size: 92px; letter-spacing: -2px;
    color: var(--navy-soft);
  }
  .tagline {
    position: absolute; left: 40px; right: 40px; bottom: 78px;
    text-align: center; font-size: 15px; color: var(--white);
  }
</style>
</head>
<body>
<main class="stage">
  <section class="card card-front" aria-label="Business card front">
    <div class="brand">
      <span class="brand-mark"></span>
      <span class="brand-name">mediqbay</span>
    </div>

    <div class="person">
      <p class="person-name">Paul Dwyer</p>
      <p class="person-role">Director</p>

      <ul class="contact-list">
        <li class="contact-item">
          <svg class="contact-icon" viewBox="0 0 14 14" aria-hidden="true"><path d="M1 4c0-2 1-3 3-3h6c2 0 3 1 3 3v1H9V3.5H5V5H1z M2 6h10l1 7H1z" fill="var(--orange)"/></svg>
          03 9472 5836
        </li>
        <li class="contact-item">
          <svg class="contact-icon" viewBox="0 0 14 14" aria-hidden="true"><rect x="3.5" y="0.5" width="7" height="13" rx="1.2" fill="var(--orange)"/><rect x="5" y="2" width="4" height="8" fill="var(--card)"/></svg>
          0438 275 904
        </li>
        <li class="contact-item">
          <svg class="contact-icon" viewBox="0 0 14 14" aria-hidden="true"><rect x="0.5" y="2.5" width="13" height="9" fill="var(--orange)"/><path d="M1 3l6 5 6-5" stroke="var(--card)" stroke-width="1.2" fill="none"/></svg>
          firstname.lastname@mediqbay.com.au
        </li>
        <li class="contact-item">
          <svg class="contact-icon" viewBox="0 0 14 14" aria-hidden="true"><rect x="3" y="0.5" width="8" height="5" fill="var(--orange)"/><rect x="0.5" y="5" width="13" height="6" rx="1" fill="var(--orange)"/><rect x="3" y="9" width="8" height="4.5" fill="var(--orange)" stroke="var(--card)"/></svg>
          03 8241 3975
        </li>
        <li class="contact-item">
          <svg class="contact-icon" viewBox="0 0 14 14" aria-hidden="true"><circle cx="7" cy="7" r="6.5" fill="var(--orange)"/><path d="M0.5 7h13M7 0.5c-3 3-3 10 0 13M7 0.5c3 3 3 10 0 13" stroke="var(--card)" stroke-width="0.9" fill="none"/></svg>
          mediqbay.com.au
        </li>
      </ul>

      <p class="address">Suite 31, 286 Keldon Street , Kestrel Bay, Avonmere</p>
    </div>

    <div class="social" aria-hidden="true">
      <span class="social-badge"></span>
      <span class="social-badge"></span>
      <span class="social-badge"></span>
      <span class="social-badge"></span>
    </div>
  </section>

  <section class="card card-back" aria-label="Business card back">
    <p class="back-name">mediqbay</p>
    <p class="tagline">“Building smarter clinical tools that lift patient care and practice efficiency”</p>
  </section>
</main>
</body>
</html>
```